Mortgage firm needs clean and simple wordpress website and logo

The competition is for design only, and the winning design for the homepage will be expected to create a second design for a simpler template for additional pages.

We need a logo and basic wordpress website design for a Sydney based mortgage firm.
We need a clean and simple logo and website, based on the mortgage/accounting/finance/tax industry. Simple, credible and official colors.

The logo is expected to be so simple that we have combined into the one job.
If you submit a logo design and we choose it along with someone else's website design you will be paid a bonus of $60. The website design will still win the competition as per normal.

Current website is old and terrible but gives you an idea of the sitemap (super simple) and what they do: http://www.loanharbourgroup.com.au/

We will integrate a mortgage calculator into the site.
The calculator is adjustable in styles, you can see it here: http://www.loanharbourgroup.com.au/mortgagecalculator/

We want original different to copy-and-paste template looking designs.
We like simple websites with a long home page and a few additional pages like https://www.homelendquest.com.au/

We are based in Sydney Australia and are mortgage brokers

We want a clean, formal, credible site, limited pages.

The project is guaranteed, so go for it.

Example of basic template after home page complete: http://loanharbourgroup.com.au/template_example.jpg

Target Market(s)

Mortgage and banking clients

Industry/Entity Type

Finance

Number of Pages Required

1 page

Requirements
Must have
• A simple logo, Wordpress capable, be able to incorporate the mortgage calculator (on the home page if needed as well as its own page)
Nice to have
• VIdeo - something free but nice

```html
<!DOCTYPE html>
<html lang="en">
<head>
<meta charset="utf-8">
<title>Loan Harbour Group — Private Funding</title>
<link href="https://fonts.googleapis.com/css2?family=Montserrat:wght@400;500&family=Open+Sans:wght@400&display=swap" rel="stylesheet">
<style>
:root{
  --white:#ffffff;
  --ink:#2f2f2f;
  --body:#6a6a6a;
  --soft:#f2f2f2;
  --blue:#0aa2f5;
  --panel:rgba(58,58,60,.88);
  --footer-top:#3b3b3b;
  --footer-bottom:#161616;
  --footer-text:#c9c9c9;
  --line:#c8c8c8;
}
*{box-sizing:border-box;margin:0;padding:0}
html,body{width:777px;height:1200px;overflow:hidden}
body{position:relative;background:var(--white);font-family:"Open Sans",Arial,sans-serif;color:var(--body)}
.heading{font-family:"Montserrat",Arial,sans-serif}
.abs{position:absolute}

/* hero */
.hero{position:absolute;left:0;top:0;width:777px;height:370px;
  background:radial-gradient(ellipse at 42% 45%,#d9b08c 0%,#b88d66 25%,#8a6a4e 55%,#5f4c3c 100%)}
.hero-shade{position:absolute;inset:0;background:linear-gradient(90deg,rgba(40,30,22,.35),rgba(40,30,22,0) 45%,rgba(40,30,22,.25))}
.logo{left:88px;top:20px;font-family:"Montserrat",Arial,sans-serif;font-size:19.5px;font-weight:400;color:var(--white);letter-spacing:.3px}
.nav{left:294px;top:22px;display:flex;align-items:center;font-family:"Montserrat",Arial,sans-serif;font-size:10px;color:var(--white)}
.nav a{color:var(--white);text-decoration:none;margin-right:24px}
.nav .current{border:1px solid var(--white);padding:7px 11px;margin-right:12px}
.nav .phone{display:flex;align-items:center;font-size:11px;margin-left:6px;margin-right:0}
.nav .phone svg{margin-right:3px}
.hero-title{left:90px;top:156px;font-family:"Montserrat",Arial,sans-serif;font-size:29px;line-height:32px;color:var(--white);font-weight:400}
.dots{left:96px;top:233px;display:flex;gap:3px}
.dots span{width:10px;height:10px;border-radius:50%;background:var(--white)}
.dots span.off{background:transparent;border:1.5px solid var(--white)}

/* calculator */
.calc{left:471px;top:96px;width:192px;height:217px;background:var(--panel);padding:14px 19px 0 19px;color:var(--white)}
.calc h2{font-family:"Montserrat",Arial,sans-serif;font-weight:400;font-size:15.5px;margin-bottom:9px}
.field-label{font-size:8px;margin-bottom:3px;font-family:"Montserrat",Arial,sans-serif}
.field{display:flex;height:20px;margin-bottom:14px;background:var(--white);font-size:7.5px;color:#555}
.field .pre{width:19px;background:#dcdcdc;display:flex;align-items:center;justify-content:center}
.field .val{flex:1;display:flex;align-items:center;padding-left:6px}
.field .unit{width:29px;background:#dcdcdc;display:flex;align-items:center;justify-content:center;font-size:6.5px;color:#777}
.calc-btn{width:156px;height:27px;background:var(--blue);color:var(--white);font-family:"Montserrat",Arial,sans-serif;font-size:11.5px;display:flex;align-items:center;justify-content:center;margin-top:-2px}

/* features */
.features{position:absolute;left:0;top:370px;width:777px;height:210px;background:var(--soft)}
.feature{position:absolute;top:331px;width:176px;text-align:center}
.pin{display:block;margin:0 auto}
.feature h3{font-family:"Montserrat",Arial,sans-serif;font-weight:400;font-size:17.5px;color:var(--ink);margin-top:4px;margin-bottom:8px}
.feature p{font-size:7.4px;line-height:12.8px;color:#555}

/* about */
.about-title{left:0;top:628px;width:777px;text-align:center;font-family:"Montserrat",Arial,sans-serif;font-size:20px;color:var(--ink);letter-spacing:.3px}
.about-text{left:100px;top:659px;width:577px;text-align:center;font-size:9.2px;line-height:16px;color:#8a8a8a}
.video-shadow{left:155px;top:880px;width:487px;height:36px;background:radial-gradient(ellipse at 50% 100%,rgba(0,0,0,.12),rgba(0,0,0,0) 70%)}
.video{left:236px;top:741px;width:309px;height:174px;background:var(--white);border:1px solid #e2e2e2;padding:5px}
.video-still{width:100%;height:100%;background:linear-gradient(180deg,#4b5a3c 0%,#6d7c56 40%,#8f9480 65%,#5d5a4a 100%);position:relative;display:flex;align-items:center;justify-content:center}
.more-btn{left:319px;top:941px;width:135px;height:38px;border:2px solid var(--line);border-radius:20px;display:flex;align-items:center;justify-content:center;font-family:"Montserrat",Arial,sans-serif;font-size:11px;color:#555}

/* footer */
.footer{position:absolute;left:0;top:1016px;width:777px;height:184px;background:linear-gradient(180deg,var(--footer-top),var(--footer-bottom))}
.footer-logo{left:87px;top:1051px;font-family:"Montserrat",Arial,sans-serif;font-size:19.5px;color:#9a9a9a}
.footer-legal{left:87px;top:1087px;font-size:8.8px;line-height:18px;color:#9a9a9a}
.footer-col{top:1045px;font-size:8.8px;line-height:19px;color:var(--footer-text)}
.footer-col h4{font-family:"Montserrat",Arial,sans-serif;font-weight:500;font-size:9.6px;color:var(--white);margin-bottom:2px}
.social{left:533px;top:1143px;display:flex;gap:8px}
.social span{width:20px;height:20px;border-radius:50%;background:#2a2a2a}
</style>
</head>
<body>

<section class="hero" role="img" aria-label="Photo of a hand holding a house key with a small wooden house keyring over a desk">
  <div class="hero-shade"></div>
</section>

<div class="abs logo">Loan Harbour Group</div>
<nav class="abs nav">
  <a class="current" href="#">Home</a>
  <a href="#">About us</a>
  <a href="#">Calculator</a>
  <a href="#">Contact Us</a>
  <a class="phone" href="#"><svg width="11" height="11" viewBox="0 0 24 24"><path fill="#fff" d="M6.6 10.8a15.1 15.1 0 0 0 6.6 6.6l2.2-2.2c.3-.3.7-.4 1-.2 1.1.4 2.3.6 3.6.6.6 0 1 .4 1 1V20c0 .6-.4 1-1 1C10.6 21 3 13.4 3 4c0-.6.4-1 1-1h3.5c.6 0 1 .4 1 1 0 1.3.2 2.5.6 3.6.1.3 0 .7-.2 1z"/></svg>(+612) 9411 5200</a>
</nav>

<h1 class="abs hero-title">Loan Harbour Group<br>Private Funding</h1>
<div class="abs dots"><span></span><span></span><span></span><span class="off"></span></div>

<aside class="abs calc">
  <h2>Mortgage Calculator</h2>
  <div class="field-label">Loan Amount</div>
  <div class="field"><span class="pre">$</span><span class="val">10000</span><span class="unit">AUD</span></div>
  <div class="field-label">Loan Term</div>
  <div class="field"><span class="pre">$</span><span class="val">30 Years</span><span class="unit">YRS</span></div>
  <div class="field-label">Loan Interest</div>
  <div class="field"><span class="pre">$</span><span class="val">6%</span><span class="unit" style="font-size:9px">%</span></div>
  <div class="calc-btn">Calculator Now</div>
</aside>

<section class="features"></section>

<div class="feature" style="left:99px">
  <svg class="pin" width="94" height="115" viewBox="0 0 94 115">
    <path d="M47 113 L12 78 A46 46 0 1 1 82 78 Z" fill="#fff" stroke="#e6e6e6"/>
    <circle cx="47" cy="40" r="19" fill="none" stroke="#444" stroke-width="1.6"/>
    <circle cx="47" cy="40" r="14" fill="none" stroke="#444" stroke-width="1.6"/>
    <path d="M38 56 V75 L47 67 L56 75 V56" fill="none" stroke="#444" stroke-width="1.6"/>
  </svg>
  <h3>Experience</h3>
  <p>Loan Harbour Group have been organising and managing money for clients for over 25 years using our access to banks, private lenders and brokers within Australia.</p>
</div>

<div class="feature" style="left:301px">
  <svg class="pin" width="94" height="115" viewBox="0 0 94 115">
    <path d="M47 113 L12 78 A46 46 0 1 1 82 78 Z" fill="#fff" stroke="#e6e6e6"/>
    <path d="M66 24 C58 24 48 30 42 40 L36 50 L45 59 L55 53 C65 47 71 37 71 29 Z" fill="none" stroke="#444" stroke-width="1.6"/>
    <circle cx="57" cy="37" r="4" fill="none" stroke="#444" stroke-width="1.6"/>
    <path d="M42 40 L33 41 L29 47 L36 50 M55 53 L54 62 L48 66 L45 59" fill="none" stroke="#444" stroke-width="1.6"/>
    <path d="M36 56 C30 56 24 62 26 68 C32 68 38 62 39 59" fill="none" stroke="#444" stroke-width="1.6"/>
  </svg>
  <h3>Fast</h3>
  <p>We can provide money in 24 Hours, providing you meet the loan criteria. Unlike banks that might take months to complete a loan, we can react to your demands quickly</p>
</div>

<div class="feature" style="left:510px">
  <svg class="pin" width="94" height="115" viewBox="0 0 94 115">
    <path d="M47 113 L12 78 A46 46 0 1 1 82 78 Z" fill="#fff" stroke="#e6e6e6"/>
    <circle cx="35" cy="35" r="11" fill="none" stroke="#444" stroke-width="1.6"/>
    <circle cx="35" cy="35" r="6" fill="none" stroke="#444" stroke-width="1.6"/>
    <path d="M43 43 L66 66 L62 70 M52 52 L49 55 M57 57 L54 60 M61 61 L58 64" fill="none" stroke="#444" stroke-width="1.6"/>
  </svg>
  <h3>Private</h3>
  <p>Our specialty is private lending for residential, commercial and industrial properties. We generally look for registered first mortgage security with up to 80% loan funding based on the property valuation, the type of security and</p>
</div>

<h2 class="abs about-title">ABOUT OUR COMPANY</h2>
<p class="abs about-text">Maecenas aliquet velit vel turpis Mauris neque metus malesuada nec ultricies sit amet porttitor mattis enim In massa libero interdum nec interdum vel blandit sed nulla In ullamcorper est eget tempor cursus neque mi consectetuer mi a ultricies massa est sed nisl Class aptent taciti sociosqu ad litora torquent per conubia nostra per inceptos hymenaeos</p>

<div class="abs video-shadow"></div>
<div class="abs video">
  <div class="video-still" role="img" aria-label="Video still of a park path lined with trees and a bench">
    <svg width="60" height="60" viewBox="0 0 60 60"><circle cx="30" cy="30" r="27" fill="none" stroke="#fff" stroke-width="3"/><path d="M24 18 L42 30 L24 42 Z" fill="none" stroke="#fff" stroke-width="3" stroke-linejoin="round"/></svg>
  </div>
</div>
<a class="abs more-btn">Watch More Videos</a>

<footer class="footer"></footer>
<div class="abs footer-logo">Loan Harbour Group</div>
<div class="abs footer-legal">© 2016 Company Name&nbsp; All right reserved<br>Term of Use &nbsp;|&nbsp; Privacy Policy</div>
<div class="abs footer-col" style="left:310px"><h4>COMPANY</h4>Home<br>About Us<br>Why Choose Us<br>Calculator</div>
<div class="abs footer-col" style="left:428px"><h4>RESOURCES</h4>Support<br>Team<br>Video<br>Contact</div>
<div class="abs footer-col" style="left:533px"><h4>CONTACT US</h4>Daniel K. Hollis +614 2270 3145<br>Stephen R. Marlow +614 2281 6409<br>Office +612 9411 5200<br>Fax +612 9411 5201</div>
<div class="abs social"><span></span><span></span><span></span><span></span></div>

</body>
</html>
```